Design needed for Cover of Conference Brochure

We are a conference company that puts on several business conferences per year. We are putting together a new conference - the Clearpath Forum Week, and our audience is UX practitioners and specialists, product designers, UX designers, etc.
We need a brochure cover created. We are looking for fresh design ideas and are open to varying color schemes - please just keep in mind that this is a conference for business professionals, and fonts and colors should reflect this. Only restriction is that we do have a general cover format that we follow - i.e. which text goes where. (I've attached samples from our other events to reference.) We also generally have a central image to each brochure - feel free to submit a few versions with different images... we want something that accurately represents UX. However, if the design is compelling enough, image might not be completely necessary. We are relatively flexible - we just want something sharp!
- Must include BWKT logo (see placing on sample event covers)
- Must include footer - see sample covers
- Red text in word document are notes to you the designer - not actual text meant to appear on the cover
This cover is standard 8x11, and will be used for web only, not print. I have attached a word doc that includes all of the text that you will need for the cover. We will need final version in PDF, jpeg, and PSD. Please message me with any questions or clarification.

```html
<!DOCTYPE html>
<html lang="en">
<head>
<meta charset="utf-8">
<title>Clearpath Forum Week – Brochure Cover</title>
<link rel="stylesheet" href="https://fonts.googleapis.com/css2?family=Anton&family=Roboto+Condensed:wght@400&family=Poppins:wght@500;600&display=swap">
<style>
  :root {
    --blue-bright: #16a3e6;
    --blue-mid: #0b6ec8;
    --blue-deep: #0a48a6;
    --navy: #1f2f92;
    --navy-dark: #150d5c;
    --yellow: #fff200;
    --white: #ffffff;
    --red: #b8321c;
    --red-dark: #7e1c0e;
  }
  * { margin: 0; padding: 0; box-sizing: border-box; }
  html, body { width: 946px; height: 1200px; overflow: hidden; }
  body { background: var(--blue-deep); font-family: "Poppins", sans-serif; }
  .cover { position: relative; width: 946px; height: 1200px; overflow: hidden; }
  .cover-shapes { position: absolute; inset: 0; }
  .title {
    position: absolute; top: 48px; left: 0; width: 100%; text-align: center;
    font-family: "Anton", sans-serif; font-size: 84px; line-height: 1;
    color: var(--yellow); letter-spacing: 0.5px;
    text-shadow: 2px 3px 6px rgba(0,0,0,0.35);
  }
  .subtitle {
    position: absolute; top: 139px; left: 0; width: 100%; text-align: center;
    font-family: "Roboto Condensed", sans-serif; font-size: 30px; color: var(--white);
  }
  .hero-art {
    position: absolute; left: 285px; top: 236px; width: 575px; height: 370px;
    border-radius: 50%;
    background: radial-gradient(circle at 45% 45%, #e3261f 0%, #f3742a 35%, #f7b52a 65%, #7bc1d8 100%);
  }
  .brand {
    position: absolute; left: 52px; top: 650px; display: flex; align-items: center; gap: 10px;
  }
  .brand-mark { width: 54px; height: 54px; border-radius: 8px; background: #6cc6f2; }
  .brand-name { font-size: 30px; font-weight: 600; color: var(--white); }
  .event-date {
    position: absolute; left: 223px; top: 698px; font-size: 27px; font-weight: 600; color: var(--yellow);
  }
  .event-venue {
    position: absolute; left: 223px; top: 734px; font-size: 22px; font-weight: 600; color: var(--yellow);
  }
  .highlights { position: absolute; left: 50px; top: 812px; list-style: none; }
  .highlights li {
    display: flex; align-items: center; gap: 8px; height: 45.5px;
    font-size: 20.5px; font-weight: 500; color: var(--white);
  }
  .tick { width: 24px; height: 24px; flex: none; }
  .early-offer {
    position: absolute; left: 542px; top: 1008px; width: 376px; height: 112px; border-radius: 50%;
    background: radial-gradient(ellipse at 50% 35%, var(--red) 0%, var(--red-dark) 100%);
    box-shadow: 0 4px 10px rgba(0,0,0,0.4);
    text-align: center; color: var(--white);
  }
  .early-offer-line { font-family: "Roboto Condensed", sans-serif; font-size: 22px; margin-top: 23px; line-height: 1.2; }
  .early-offer-amount { font-family: "Anton", sans-serif; font-size: 42px; line-height: 1.15; }
  .footer-cta {
    position: absolute; left: 36px; top: 1134px; font-size: 32px; font-weight: 600; color: var(--yellow);
  }
  .footer-web {
    position: absolute; left: 328px; top: 1150px; display: flex; align-items: center; gap: 6px;
    font-size: 16px; color: var(--white);
  }
  .footer-phone {
    position: absolute; left: 662px; top: 1138px; display: flex; align-items: center; gap: 6px;
    font-size: 31px; font-weight: 600; color: var(--white);
  }
  .icon { flex: none; }
</style>
</head>
<body>
<main class="cover">
  <svg class="cover-shapes" width="946" height="1200" viewBox="0 0 946 1200" aria-hidden="true">
    <defs>
      <radialGradient id="skyGlow" cx="0.5" cy="0.35" r="0.8">
        <stop offset="0" stop-color="#16a3e6"/>
        <stop offset="0.55" stop-color="#0b6ec8"/>
        <stop offset="1" stop-color="#0a48a6"/>
      </radialGradient>
      <linearGradient id="bandFill" x1="0" y1="0" x2="1" y2="0">
        <stop offset="0" stop-color="#2a3fa6"/>
        <stop offset="1" stop-color="#150d5c"/>
      </linearGradient>
    </defs>
    <rect width="946" height="1200" fill="url(#skyGlow)"/>
    <path class="swoosh-navy" d="M0,343 C50,430 160,540 330,610 C500,670 750,695 946,700 L946,718 C700,712 420,680 250,628 C150,600 60,560 0,520 Z" fill="#1f2f92"/>
    <path class="swoosh-line" d="M0,343 C40,420 90,475 150,515" fill="none" stroke="#ffffff" stroke-width="5"/>
    <path class="swoosh-white" d="M946,203 C600,212 200,240 110,320 C60,365 70,430 150,500 C230,570 400,640 600,672 C750,692 870,698 946,700 Z" fill="#ffffff"/>
    <path class="info-band" d="M0,757 C300,800 700,790 946,739 L946,1032 C700,1098 300,1118 0,1088 Z" fill="url(#bandFill)"/>
  </svg>

  <h1 class="title">Clearpath Forum Week</h1>
  <p class="subtitle">Design Compelling Experiences through Successful UX Strategy</p>

  <div class="hero-art" role="img" aria-label="Illustration of colourful interlocking gears forming the shape of a brain"></div>

  <div class="brand">
    <span class="brand-mark"></span>
    <span class="brand-name">BWKT</span>
  </div>

  <p class="event-date">June 10-12, 2014</p>
  <p class="event-venue">Harborview Club &amp; Hotel San Francisco, CA</p>

  <ul class="highlights">
    <li><svg class="tick" viewBox="0 0 24 24"><circle cx="11" cy="13" r="10" fill="#fff"/><path d="M6,12 L10,17 L20,3" fill="none" stroke="#d4202a" stroke-width="3"/><circle cx="11" cy="13" r="6" fill="none" stroke="#2f9b3a" stroke-width="2"/></svg>Case Studies from Leading Brands on Executing an Effective UX Strategy</li>
    <li><svg class="tick" viewBox="0 0 24 24"><circle cx="11" cy="13" r="10" fill="#fff"/><path d="M6,12 L10,17 L20,3" fill="none" stroke="#d4202a" stroke-width="3"/><circle cx="11" cy="13" r="6" fill="none" stroke="#2f9b3a" stroke-width="2"/></svg>Learn How UX-Driven Innovation Can Change Your Business</li>
    <li><svg class="tick" viewBox="0 0 24 24"><circle cx="11" cy="13" r="10" fill="#fff"/><path d="M6,12 L10,17 L20,3" fill="none" stroke="#d4202a" stroke-width="3"/><circle cx="11" cy="13" r="6" fill="none" stroke="#2f9b3a" stroke-width="2"/></svg>Build a Successful UX Team that Operates Strategically</li>
    <li><svg class="tick" viewBox="0 0 24 24"><circle cx="11" cy="13" r="10" fill="#fff"/><path d="M6,12 L10,17 L20,3" fill="none" stroke="#d4202a" stroke-width="3"/><circle cx="11" cy="13" r="6" fill="none" stroke="#2f9b3a" stroke-width="2"/></svg>Insights into UX Research, User Behavior, Usability Testing, Lean UX, and More</li>
  </ul>

  <div class="early-offer">
    <p class="early-offer-line">Register by March 7th, 2014 and</p>
    <p class="early-offer-amount">save $400!</p>
  </div>

  <p class="footer-cta">Register Today!</p>
  <p class="footer-web">
    <svg class="icon" width="20" height="20" viewBox="0 0 20 20" fill="none" stroke="#fff" stroke-width="1.3"><circle cx="10" cy="10" r="8"/><ellipse cx="10" cy="10" rx="3.5" ry="8"/><path d="M2,10 H18 M3.5,6 H16.5 M3.5,14 H16.5"/></svg>
    www.clearpathforumweek.com
  </p>
  <p class="footer-phone">
    <svg class="icon" width="28" height="28" viewBox="0 0 28 28" fill="none" stroke="#fff" stroke-width="1.6"><circle cx="14" cy="14" r="12"/><path d="M10,7 C7,10 8,16 12,20 C14,22 17,22 19,20 L17,17 L15,18 C13,16 12,14 12,12 L14,11 Z" fill="#fff"/></svg>
    888.555.0142
  </p>
</main>
</body>
</html>
```